Exercise Physiologist needs business cards

I have a logo, I need business cards (Sole trader) as I am moving to a new location and would like an updated look. I provide gym based exercise rehabilitation, injury prevention and movement assessments. I have over 13 years experience as an Exercise Physiologist. I would like the cards to look professional but not boring and can be a little different to stand out when sitting with other Allied Health Professional cards.

Target Market(s)

GP's, Allied health practitioners, people with injuries wanting to exercise

Industry/Entity Type

Health And Wellness

Contact Information for Business Card

Megan Trowbridge - Exercise Physiologist 0487 926 350
52 Wattlebird Lane
Kestrel Bay
(Door 4, Brennock Fitness)
vornalhealth@mailbox-example.com
facebook.com/Vornal

Requirements
Must have
• I would like to include a section to add next appointment date and time space to the back of the card.
Nice to have
• Rounded corners and a black background on 1 or 2 sides.
Should not have
• Pictures of fit/toned bodies etc

```html
<!DOCTYPE html>
<html lang="en">
<head>
<meta charset="utf-8">
<title>Vornal – Business Card</title>
<link href="https://fonts.googleapis.com/css2?family=Arimo:ital,wght@0,400;0,700;1,400&family=Quicksand:wght@500&display=swap" rel="stylesheet">
<style>
  :root{
    --bg:#2b2b2d;
    --card:#f7f7f8;
    --blue-dark:#1158c7;
    --blue-mid:#2a78d6;
    --blue-light:#5fb0e4;
    --ink:#4a4a4a;
    --dots:#8a8a8a;
    --white:#ffffff;
  }
  *{box-sizing:border-box;margin:0;padding:0}
  html,body{width:1200px;height:911px;overflow:hidden}
  body{background:var(--bg);font-family:"Arimo",Arial,sans-serif;position:relative}

  .card{position:absolute;width:520px;height:297px;background:var(--card);
        box-shadow:0 10px 30px rgba(0,0,0,.45);overflow:hidden}
  .card--front{left:50px;top:307px}
  .card--back{left:630px;top:307px}

  /* front */
  .contact-panel{position:absolute;left:278px;top:0;width:204px;height:228px;
        background:linear-gradient(135deg,var(--blue-mid),var(--blue-dark));
        color:var(--white);padding:28px 12px 0 18px}
  .contact-name{font-weight:700;font-size:14px;text-transform:uppercase;letter-spacing:.2px;line-height:1.15;white-space:nowrap}
  .contact-role{font-size:11px;text-transform:uppercase;margin-bottom:14px;white-space:nowrap}
  .contact-address{font-size:10.5px;line-height:1.4;margin-bottom:12px;white-space:nowrap}
  .contact-line{display:flex;align-items:center;gap:6px;font-size:10px;line-height:1.65;white-space:nowrap}
  .contact-line svg{width:9px;height:9px;flex:none}

  .brand{position:absolute;left:34px;top:172px;display:flex;align-items:center;gap:10px}
  .brand-dot{width:40px;height:40px;border-radius:50%;background:var(--blue-light)}
  .brand-name{font-family:"Quicksand",sans-serif;font-weight:500;font-size:40px;color:var(--blue-dark);line-height:1}

  .accent-bar{position:absolute;left:0;bottom:0;width:150px;height:11px;background:var(--blue-light)}

  /* back */
  .appt-title{position:absolute;left:0;right:0;top:32px;text-align:center;
        font-weight:700;font-size:19px;color:var(--blue-dark)}
  .appt-fields{position:absolute;left:40px;right:40px;top:84px}
  .appt-row{display:flex;align-items:flex-end;gap:8px;height:30px;font-size:13px;
        font-style:italic;color:var(--blue-dark)}
  .appt-row .fill{flex:1;border-bottom:1.5px dotted var(--dots);height:14px}
  .appt-row .suffix{font-size:9px;font-style:normal}
  .appt-note-line{height:30px;border-bottom:1.5px dotted var(--dots)}
  .appt-policy{position:absolute;left:30px;right:30px;bottom:20px;text-align:center;
        font-size:9.5px;font-style:italic;color:var(--ink);line-height:1.4}
</style>
</head>
<body>

<section class="card card--front" aria-label="Business card front">
  <div class="contact-panel">
    <p class="contact-name">Megan Trowbridge</p>
    <p class="contact-role">Exercise Physiologist</p>
    <p class="contact-address">52 Wattlebird Lane<br>Kestrel Bay<br>(Door 4, Brennock Fitness)</p>
    <p class="contact-line">
      <svg viewBox="0 0 10 10" aria-hidden="true"><path fill="#fff" d="M2 0.5l1.6 2.2-1 1c.6 1.3 1.5 2.2 2.8 2.8l1-1L8.6 7 7.6 9C4 8.6 1.4 6 1 2.4z"/></svg>
      0487 926 350</p>
    <p class="contact-line">
      <svg viewBox="0 0 10 10" aria-hidden="true"><rect x="0.5" y="2" width="9" height="6" fill="#fff"/><path d="M0.5 2l4.5 3.5L9.5 2" fill="none" stroke="#1158c7" stroke-width="0.9"/></svg>
      name@vornal-example.com</p>
    <p class="contact-line">
      <svg viewBox="0 0 10 10" aria-hidden="true"><circle cx="5" cy="5" r="4.5" fill="#fff"/><path d="M0.5 5h9M5 .5c-2 2.5-2 6.5 0 9M5 .5c2 2.5 2 6.5 0 9" fill="none" stroke="#1158c7" stroke-width="0.7"/></svg>
      www.vornal-example.com</p>
  </div>

  <div class="brand">
    <span class="brand-dot" aria-hidden="true"></span>
    <span class="brand-name">vornal</span>
  </div>

  <div class="accent-bar"></div>
</section>

<section class="card card--back" aria-label="Business card back">
  <h2 class="appt-title">Next Appointment</h2>
  <div class="appt-fields">
    <div class="appt-row"><span>Name :</span><span class="fill"></span></div>
    <div class="appt-row"><span>Date :</span><span class="fill"></span><span>Time :</span><span class="fill"></span><span class="suffix">AM/PM</span></div>
    <div class="appt-row"><span>Note :</span><span class="fill"></span></div>
    <div class="appt-note-line"></div>
  </div>
  <p class="appt-policy">Please give me 24 hours notice if you are unable to keep your appointment or<br>a cancellation fee may be charged.</p>
</section>

</body>
</html>
```